Modern Attractive Letterhead for Veterinary House Call Business.

A letterhead which can be printed on A4, A5 and A6 paper sizes.
To have: ( our files to be uploaded)
1. Logo with Text
2. telephone
3. email
4. website
5. Address

Target Market(s)

60-85year mainly women pet owners. Also market include families, young professionals, busy people who have dogs and cats

Industry/Entity Type

Business

Requirements
Must have
• 1. Logo with Text ( provided)
• 2. telephone
• 3. email
• 4. website
• 5. Address
Nice to have
• Needs to be modern, preferably warm and caring in nature( if possible )
Should not have
• difficulty in printing A5 and A6

```html
<!DOCTYPE html>
<html lang="en">
<head>
<meta charset="utf-8">
<title>Hearthside Vet Care – Letterhead</title>
<link href="https://fonts.googleapis.com/css2?family=Cinzel:wght@400;600&display=swap" rel="stylesheet">
<style>
  :root {
    --blue-deep: #1b3fae;
    --blue-mid: #2f7fd9;
    --blue-light: #52d3f7;
    --green: #5cc21f;
    --ink: #1f2430;
    --paper: #ffffff;
    --mark-tint: #dfe6f3;
  }
  html, body {
    margin: 0;
    padding: 0;
    width: 953px;
    height: 1200px;
    overflow: hidden;
    background: var(--paper);
  }
  .letterhead {
    position: relative;
    width: 953px;
    height: 1200px;
    background: var(--paper);
    font-family: "Cinzel", "Trajan Pro", serif;
    color: var(--ink);
  }
  .header-band {
    position: absolute;
    left: 0; top: 0;
    width: 953px; height: 74px;
    background: linear-gradient(90deg, var(--blue-deep) 0%, var(--blue-mid) 30%, var(--blue-light) 50%, var(--blue-mid) 70%, var(--blue-deep) 100%);
  }
  .header-rule {
    position: absolute;
    top: 78px;
    height: 3px;
    background: var(--green);
  }
  .header-rule.left { left: 0; width: 250px; }
  .header-rule.right { right: 0; width: 250px; }
  .brand-oval {
    position: absolute;
    left: 246px; top: 14px;
    width: 460px; height: 110px;
    border-radius: 50%;
    background: var(--paper);
  }
  .brand {
    position: absolute;
    left: 246px; top: 48px;
    width: 460px;
    display: flex;
    align-items: center;
    justify-content: center;
    gap: 12px;
  }
  .brand-dot {
    width: 30px; height: 30px;
    border-radius: 50%;
    background: var(--blue-mid);
  }
  .brand-name {
    font-size: 34px;
    font-weight: 600;
    color: var(--blue-deep);
    letter-spacing: 1px;
    white-space: nowrap;
  }
  .brand-watermark {
    position: absolute;
    left: 290px; top: 500px;
    width: 360px; height: 560px;
    border-radius: 45% 45% 40% 40%;
    background: radial-gradient(ellipse at 60% 35%, #f3f7fc 0%, var(--mark-tint) 70%, rgba(223,230,243,0) 100%);
  }
  .address {
    position: absolute;
    left: 0; top: 1084px;
    width: 953px;
    display: flex;
    justify-content: center;
    align-items: center;
    gap: 10px;
    font-size: 20px;
    letter-spacing: 1px;
  }
  .footer-rule {
    position: absolute;
    left: 108px; top: 1126px;
    width: 740px; height: 2px;
    background: linear-gradient(90deg, rgba(27,63,174,0) 0%, var(--blue-deep) 20%, var(--blue-mid) 50%, var(--blue-deep) 80%, rgba(27,63,174,0) 100%);
  }
  .contact {
    position: absolute;
    top: 1148px;
    display: flex;
    align-items: center;
    gap: 8px;
    font-size: 16px;
    white-space: nowrap;
  }
  .contact.phone { left: 72px; }
  .contact.email { left: 244px; }
  .contact.web { left: 565px; }
  .icon { display: block; }
</style>
</head>
<body>
  <main class="letterhead">
    <div class="header-band"></div>
    <div class="header-rule left"></div>
    <div class="header-rule right"></div>
    <div class="brand-oval"></div>
    <div class="brand">
      <span class="brand-dot"></span>
      <span class="brand-name">Hearthside Vet Care</span>
    </div>

    <div class="brand-watermark" role="img" aria-label="Faint brand emblem watermark"></div>

    <div class="address">
      <svg class="icon" width="26" height="24" viewBox="0 0 26 24" aria-hidden="true">
        <path d="M13 2 L24 12 H20 V22 H6 V12 H2 Z" fill="var(--blue-mid)"/>
        <rect x="11" y="15" width="4" height="7" fill="#fff"/>
      </svg>
      <span>Po Box 3841 Riverbend Qld 4070</span>
    </div>

    <div class="footer-rule"></div>

    <div class="contact phone">
      <svg class="icon" width="18" height="18" viewBox="0 0 18 18" aria-hidden="true">
        <circle cx="9" cy="9" r="8" fill="none" stroke="var(--green)" stroke-width="1.5"/>
        <path d="M6 5 Q5 9 8 12 Q10 13.5 12 13 L11 11 L9.5 11.3 Q7.5 9.5 7.8 7.5 L8.8 6.5 Z" fill="var(--green)"/>
      </svg>
      <span>0400123456</span>
    </div>
    <div class="contact email">
      <svg class="icon" width="18" height="13" viewBox="0 0 18 13" aria-hidden="true">
        <rect x="0" y="0" width="18" height="13" fill="var(--green)"/>
        <path d="M0 0 L9 7 L18 0" fill="none" stroke="#fff" stroke-width="1.4"/>
      </svg>
      <span>Hello@hearthsidevet.com.au</span>
    </div>
    <div class="contact web">
      <svg class="icon" width="19" height="19" viewBox="0 0 19 19" aria-hidden="true">
        <g fill="none" stroke="var(--green)" stroke-width="1.4">
          <circle cx="9.5" cy="9.5" r="8"/>
          <ellipse cx="9.5" cy="9.5" rx="3.5" ry="8"/>
          <line x1="1.5" y1="9.5" x2="17.5" y2="9.5"/>
          <path d="M3 5 H16 M3 14 H16"/>
        </g>
      </svg>
      <span>Www.hearthsidevet.com.au</span>
    </div>
  </main>
</body>
</html>
```